Velmora Strom GmbH webpage The online Business card of a master electrician

A clean, modern webpage on whitch i can show my clients what im capable of and where the future costumer can inform himself. I need a login page for costumers who are registred and an secound webpage where my stuff can login to report theyr labour.
I will post pictures before and after, put on some commercial and crossellimg informations.
The costumer should find my insta as well my twitter or snapchat accounts.

Update:
Our Services are, Installations, Renovations, Home Automation, CCTV, Telefon / VOIP, Networking / Network-Cabeling, Electrical Supervisioning

Target Market(s)

Private and business costumers

Industry/Entity Type

Electric Company

Number of Pages Required

5+ page

Font styles to use
Sans Serif
Other font styles liked:
• Zurich,

Colors

Designer to choose colors to be used in the design.

Requirements
Must have
• A Page Hero
• A Costumer and staff login page (2separate pages)
• Contact form
• Responsive form
• Instagram enbedding account velmora_strom
Nice to have
• A Blog

```html
<!DOCTYPE html>
<html lang="en">
<head>
<meta charset="utf-8">
<title>Velmora Strom GmbH – Electrical Services</title>
<link rel="stylesheet" href="https://fonts.googleapis.com/css2?family=Roboto:wght@400;500;700&family=Roboto+Slab:wght@300;400;700&display=swap">
<style>
:root{
  --blue:#1e9ad6;
  --blue-deep:#1a87c4;
  --navy:#2b4d9c;
  --navy-dark:#17284f;
  --sky-line:#8fb6dd;
  --text:#4a4a4a;
  --white:#ffffff;
  --black:#141414;
}
*{box-sizing:border-box;margin:0;padding:0}
html,body{width:1200px;height:2281px;overflow:hidden}
body{position:relative;font-family:"Roboto",Arial,sans-serif;color:var(--text);background:var(--white)}
.abs{position:absolute}
.slab{font-family:"Roboto Slab",Georgia,serif}

/* hero */
.hero{left:0;top:0;width:1200px;height:563px;background:linear-gradient(180deg,#c96a12 0%,#e08a1c 35%,#d4761a 62%,#8a3a0c 88%,#2a1406 100%)}
.hero-ground{left:0;top:520px;width:1200px;height:43px;background:linear-gradient(180deg,rgba(20,10,4,0) 0%,#1a0d05 100%)}
.logo-box{left:161px;top:0;width:252px;height:91px;background:var(--white);display:flex;align-items:center;justify-content:flex-start;gap:8px;padding-left:16px;z-index:2;clip-path:polygon(0 0,100% 0,88% 100%,0 100%)}
.logo-box .mark{width:18px;height:18px;background:var(--blue);flex:none}
.logo-box .name{font-family:"Roboto",Arial,sans-serif;font-weight:700;font-size:20px;color:var(--navy);white-space:nowrap}
.topbar{left:432px;top:13px;width:607px;height:20px;color:var(--white);font-size:15px;display:flex;align-items:center}
.topbar .phone{display:flex;align-items:center;gap:8px}
.topbar .auth{margin-left:auto;display:flex;gap:18px;align-items:center;font-size:13px}
.topbar .auth span{display:flex;align-items:center;gap:6px}
.social{display:flex;gap:8px;margin-left:14px}
.social i{width:22px;height:22px;border:2px solid var(--white);border-radius:50%;display:block}
.nav{left:373px;top:41px;width:666px;height:50px;background:var(--blue);display:flex;align-items:center;justify-content:space-around;padding:0 8px 0 40px;z-index:1}
.nav a{color:var(--white);text-decoration:none;font-size:13px;font-weight:500}
.hero-title{left:161px;top:255px;color:var(--white);font-size:44px;font-weight:700;line-height:1;white-space:nowrap}
.hero-sub{left:161px;top:302px;color:var(--white);font-size:28px;font-weight:300;line-height:1;white-space:nowrap}
.btn-more{left:161px;top:360px;width:123px;height:37px;background:var(--blue);border:2px solid var(--white);color:var(--white);font-size:15px;display:flex;align-items:center;justify-content:center;gap:7px}
.arrow-btn{top:311px;width:36px;height:36px;border:2px solid var(--white);border-radius:50%;display:flex;align-items:center;justify-content:center}

/* contact */
.contact{left:707px;top:134px;width:332px;height:380px;background:rgba(70,40,5,.55)}
.contact h2{height:52px;background:var(--navy);color:var(--white);font-family:"Roboto Slab",Georgia,serif;font-weight:700;font-size:30px;text-align:center;line-height:52px}
.field-label{left:17px;color:var(--white);font-size:12px;font-weight:700;line-height:14px;width:60px}
.field{left:79px;width:235px;background:var(--white)}
.submit{left:79px;top:330px;width:111px;height:29px;background:var(--black);border-radius:15px;color:var(--white);font-size:11px;font-weight:700;display:flex;align-items:center;justify-content:center;gap:6px}

/* band */
.band{left:0;top:563px;width:1200px;height:61px;background:var(--navy)}
.band p{position:absolute;left:161px;top:19px;color:var(--white);font-size:21px}
.btn-service{left:917px;top:17px;width:120px;height:28px;border:2px solid var(--white);border-radius:14px;color:var(--white);font-size:14px;display:flex;align-items:center;justify-content:center;gap:6px}

/* welcome */
.welcome{left:0;top:624px;width:1200px;height:423px;background:#fbfbfb}
.welcome-photo{left:213px;top:35px;width:414px;height:289px;background:linear-gradient(135deg,#d9dde0 0%,#9ea7ad 45%,#5e6a73 100%);border:4px solid #eeeeee}
.welcome-card{left:575px;top:89px;width:417px;height:299px;background:var(--blue);border:4px solid var(--blue-deep);outline:1px solid rgba(255,255,255,.6);outline-offset:-10px;color:var(--white);text-align:center}
.welcome-card .pre{margin-top:78px;font-family:"Roboto Slab",Georgia,serif;font-weight:300;font-size:24px}
.welcome-card h3{font-family:"Roboto Slab",Georgia,serif;font-weight:700;font-size:36px;line-height:1.1;white-space:nowrap}
.welcome-card p{margin:20px auto 0;width:370px;font-size:11px;line-height:1.45}

/* services */
.services{left:0;top:1047px;width:1200px;height:448px;background:linear-gradient(90deg,#1b2c57 0%,#2d4373 45%,#4d6392 70%,#3b4f7c 100%)}
.services .kicker{left:161px;top:97px;color:var(--white);font-family:"Roboto Slab",Georgia,serif;font-size:21px;white-space:nowrap}
.services h2{left:161px;top:116px;color:var(--white);font-family:"Roboto Slab",Georgia,serif;font-weight:700;font-size:40px;line-height:1}
.services .rule{left:356px;top:139px;width:289px;height:1px;background:rgba(255,255,255,.7)}
.services .lead{left:161px;top:174px;width:580px;color:var(--white);font-size:12px;line-height:1.45}
.svc{top:246px;height:129px;border:1px solid rgba(255,255,255,.55);color:var(--white);font-size:17px;text-align:center}
.svc .ic{position:absolute;left:50%;top:12px;transform:translateX(-50%)}
.svc span{position:absolute;left:0;right:0;bottom:12px;white-space:nowrap}

/* cta */
.cta{left:0;top:1495px;width:1200px;height:81px;background:var(--navy)}
.cta p{position:absolute;left:161px;top:30px;color:var(--white);font-size:21px;white-space:nowrap}
.cta .right{position:absolute;left:0;top:0}
.cta .consult{position:absolute;left:833px;top:23px;color:var(--white);font-size:22px;display:flex;align-items:center;gap:7px}

/* feedback */
.feedback{left:0;top:1576px;width:1200px;height:386px;background:#fafbfc}
.feedback h2{left:0;width:1200px;top:66px;text-align:center;color:var(--blue);font-family:"Roboto Slab",Georgia,serif;font-weight:700;font-size:34px}
.fb-line{top:85px;height:1px;background:var(--sky-line)}
.quote{top:162px;width:326px;height:110px;border:1px solid var(--blue);background:var(--white);padding:17px 13px;font-size:11px;line-height:1.4}
.avatar{top:160px;width:62px;height:62px;border-radius:50%;border:3px solid var(--blue);background:linear-gradient(180deg,#c9ccd1,#6f7780)}
.person{top:228px;width:76px;text-align:center}
.person b{display:block;color:var(--blue);font-family:"Roboto Slab",Georgia,serif;font-size:11px;white-space:nowrap}
.person small{font-size:11px;color:#555}
.pager{top:328px;width:27px;height:27px;background:#4e58a6;display:flex;align-items:center;justify-content:center}

/* footer */
.footer{left:0;top:1962px;width:1200px;height:285px;background:var(--navy);color:var(--white)}
.footer-logo{left:161px;top:91px;width:260px;height:85px;border:1px solid rgba(255,255,255,.8);display:flex;align-items:center;justify-content:center;gap:10px}
.footer-logo .mark{width:20px;height:20px;background:var(--white)}
.footer-logo .name{font-weight:700;font-size:24px}
.footer h4{font-weight:400;font-size:18px}
.footer .rule{height:1px;background:rgba(255,255,255,.35)}
.footer .about{left:464px;top:98px;width:286px;font-size:11px;line-height:1.45}
.footer .row{left:809px;display:flex;align-items:center;gap:10px;font-size:18px}
.footer .row small{font-size:12px}
.footer .connect{left:464px;top:216px;display:flex;align-items:center;gap:10px;font-size:16px}
.footer .connect i{width:23px;height:23px;border-radius:50%;background:var(--white);display:block}
.copyright{left:0;top:2247px;width:1200px;height:34px;background:var(--blue);color:var(--white);font-size:12px;text-align:center;line-height:34px}
</style>
</head>
<body>

<section class="hero abs" role="img" aria-label="Photo of electricity pylons and power lines against an orange sunset sky"></section>
<div class="hero-ground abs"></div>

<header>
  <div class="logo-box abs"><i class="mark"></i><span class="name">Velmora Strom</span></div>
  <div class="topbar abs">
    <span class="phone"><svg width="13" height="13" viewBox="0 0 24 24"><path fill="#fff" d="M6.6 10.8a15 15 0 0 0 6.6 6.6l2.2-2.2c.3-.3.7-.4 1-.2 1.1.4 2.3.6 3.6.6.6 0 1 .4 1 1V20c0 .6-.4 1-1 1A17 17 0 0 1 3 4c0-.6.4-1 1-1h3.5c.6 0 1 .4 1 1 0 1.3.2 2.5.6 3.6.1.3 0 .7-.2 1z"/></svg>(000) 000-0000</span>
    <div class="auth">
      <span><svg width="12" height="12" viewBox="0 0 24 24"><path fill="#fff" d="M10 17l5-5-5-5v3H2v4h8zM13 3h7v18h-7v-2h5V5h-5z"/></svg>LOGIN</span>
      <span><svg width="11" height="12" viewBox="0 0 24 24"><circle cx="12" cy="7" r="5" fill="#fff"/><path fill="#fff" d="M2 22c0-6 4-9 10-9s10 3 10 9z"/></svg>REGISTER</span>
    </div>
    <div class="social"><i></i><i></i><i></i></div>
  </div>
  <nav class="nav abs">
    <a href="#">HOME</a><a href="#">ABOUT</a><a href="#">SERVICES</a><a href="#">TESTIMONAILS</a><a href="#">NEWS</a><a href="#">CONTACT US</a>
  </nav>
</header>

<h1 class="hero-title abs slab">VELMORA STROM</h1>
<p class="hero-sub abs slab">BEST ELECTRICAL SERVICES</p>
<div class="btn-more abs"><svg width="12" height="16" viewBox="0 0 12 16"><path fill="#fff" d="M7 0L0 9h5l-1 7 8-10H7z"/></svg>Know More</div>
<div class="arrow-btn abs" style="left:23px"><svg width="8" height="12" viewBox="0 0 8 12"><path d="M7 1L2 6l5 5" fill="none" stroke="#fff" stroke-width="2"/></svg></div>
<div class="arrow-btn abs" style="left:1142px"><svg width="8" height="12" viewBox="0 0 8 12"><path d="M1 1l5 5-5 5" fill="none" stroke="#fff" stroke-width="2"/></svg></div>

<form class="contact abs">
  <h2>CONTACT US</h2>
  <label class="field-label abs" style="top:79px">Name:</label><div class="field abs" style="top:73px;height:30px"></div>
  <label class="field-label abs" style="top:117px">Email:</label><div class="field abs" style="top:111px;height:30px"></div>
  <label class="field-label abs" style="top:153px">Phone:</label><div class="field abs" style="top:147px;height:31px"></div>
  <label class="field-label abs" style="top:184px">Delivery Suburb:</label><div class="field abs" style="top:181px;height:30px"></div>
  <label class="field-label abs" style="top:225px">Message:</label><div class="field abs" style="top:219px;height:91px"></div>
  <div class="submit abs"><svg width="12" height="8" viewBox="0 0 12 8"><path d="M0 4h10M7 1l3 3-3 3" stroke="#fff" stroke-width="1.6" fill="none"/></svg>SUBMIT NOW!</div>
</form>

<section class="band abs">
  <p>LOOKING FOR AN ELECTRICAL SERVICE</p>
  <div class="btn-service abs"><svg width="13" height="13" viewBox="0 0 14 14"><circle cx="7" cy="7" r="6" fill="#fff"/><path d="M6 4l3 3-3 3" stroke="#2b4d9c" stroke-width="1.8" fill="none"/></svg>GET SERVICE</div>
</section>

<section class="welcome abs">
  <div class="welcome-photo abs" role="img" aria-label="Photo of two electricians in hard hats working at an open switchboard"></div>
  <div class="welcome-card abs">
    <svg class="abs" style="left:180px;top:28px" width="40" height="52" viewBox="0 0 12 16"><path fill="#fff" d="M8 0L1 9h4l-2 7 8-10H7z"/></svg>
    <p class="pre">Welcome to</p>
    <h3>VELMORA STROM</h3>
    <p>Velmora Strom is a master electrician business serving private and business customers. We plan, install and maintain electrical systems with care, from a single socket to a complete building. Every job is documented, tested and handed over clean, so you always know what was done and why it matters for your safety.</p>
  </div>
</section>

<section class="services abs" role="img" aria-label="Photo of a smiling electrician in a hard hat in front of a distribution board, tinted blue">
  <p class="kicker abs">VELMORA STROM</p>
  <svg class="abs" style="left:336px;top:72px" width="40" height="56" viewBox="0 0 12 16"><path fill="#fff" d="M8 0L1 9h4l-2 7 8-10H7z"/></svg>
  <h2 class="abs">SERVICES:</h2>
  <div class="rule abs"></div>
  <p class="lead abs">From installations and renovations to home automation, CCTV and network cabling, our team delivers safe, certified work on every project.</p>

  <div class="svc abs" style="left:160px;width:109px">
    <svg class="ic" width="70" height="80" viewBox="0 0 70 80"><rect x="1" y="0" width="68" height="66" fill="#1e9ad6"/><path d="M27 66h16l-8 12z" fill="#1e9ad6"/><path d="M24 14h22l5 18H19z" fill="#fff"/><rect x="33" y="32" width="4" height="16" fill="#fff"/><rect x="24" y="48" width="22" height="4" fill="#fff"/></svg>
    <span>Electrical</span>
  </div>
  <div class="svc abs" style="left:292px;width:110px">
    <svg class="ic" width="70" height="80" viewBox="0 0 70 80"><rect x="1" y="0" width="68" height="66" fill="#1e9ad6"/><path d="M27 66h16l-8 12z" fill="#1e9ad6"/><g fill="#fff"><rect x="18" y="26" width="6" height="28" rx="3"/><rect x="27" y="26" width="6" height="28" rx="3"/><rect x="36" y="26" width="6" height="28" rx="3"/><rect x="45" y="26" width="6" height="28" rx="3"/></g><path d="M22 10q2 4 0 8M31 10q2 4 0 8M40 10q2 4 0 8M49 10q2 4 0 8" stroke="#fff" stroke-width="2" fill="none"/></svg>
    <span>Heating</span>
  </div>
  <div class="svc abs" style="left:424px;width:137px">
    <svg class="ic" width="70" height="80" viewBox="0 0 70 80"><rect x="1" y="0" width="68" height="66" fill="#1e9ad6"/><path d="M27 66h16l-8 12z" fill="#1e9ad6"/><rect x="14" y="14" width="42" height="38" fill="#fff"/><circle cx="35" cy="33" r="12" fill="none" stroke="#1e9ad6" stroke-width="3"/><path d="M35 21v24M23 33h24" stroke="#1e9ad6" stroke-width="2"/></svg>
    <span>Air Conditioning</span>
  </div>
  <div class="svc abs" style="left:584px;width:152px">
    <svg class="ic" width="70" height="80" viewBox="0 0 70 80"><rect x="1" y="0" width="68" height="66" fill="#1e9ad6"/><path d="M27 66h16l-8 12z" fill="#1e9ad6"/><rect x="12" y="16" width="46" height="26" fill="#fff"/><path d="M18 20v8M24 20v8M30 20v8M36 20v8M42 20v8M48 20v8" stroke="#1e9ad6" stroke-width="2"/><path d="M36 30l-5 7h4l-2 5 6-7h-4z" fill="#1e9ad6"/><rect x="26" y="42" width="18" height="6" fill="#fff"/></svg>
    <span>Security Systems</span>
  </div>
</section>

<section class="cta abs">
  <svg class="right" width="1200" height="81" viewBox="0 0 1200 81"><path d="M818 0H1200V81H818L806 40z" fill="#1e9ad6"/></svg>
  <p>IF YOU FIND A HIGH QUALITY ELECTRICAL FOR YOUR PROJECTS</p>
  <svg class="abs" style="left:710px;top:12px" width="18" height="26" viewBox="0 0 12 16"><path fill="#fff" d="M8 0L1 9h4l-2 7 8-10H7z"/></svg>
  <div class="consult"><svg width="16" height="16" viewBox="0 0 14 14"><circle cx="7" cy="7" r="6.5" fill="#fff"/><path d="M6 4l3 3-3 3" stroke="#1e9ad6" stroke-width="1.8" fill="none"/></svg>GET A FREE COSULT</div>
</section>

<section class="feedback abs">
  <div class="fb-line abs" style="left:289px;width:137px"></div>
  <div class="fb-line abs" style="left:760px;width:150px"></div>
  <h2 class="abs">CLIENT FEED BACK</h2>
  <svg class="abs" style="left:752px;top:38px" width="26" height="38" viewBox="0 0 12 16"><path fill="#1e9ad6" d="M8 0L1 9h4l-2 7 8-10H7z"/></svg>

  <div class="quote abs" style="left:161px">The team rewired our whole flat in two days, kept everything tidy and explained each step. Clear prices, no surprises and a friendly crew we would gladly book again.</div>
  <svg class="abs" style="left:486px;top:176px" width="10" height="18" viewBox="0 0 10 18"><path d="M0 0l9 9-9 9" fill="#fff" stroke="#1e9ad6"/></svg>
  <div class="quote abs" style="left:713px">Our office network and camera system were installed on time and fully documented. Support has been quick whenever we needed a change, which keeps our business running.</div>
  <svg class="abs" style="left:705px;top:176px" width="10" height="18" viewBox="0 0 10 18"><path d="M10 0L1 9l9 9" fill="#fff" stroke="#1e9ad6"/></svg>

  <div class="avatar abs" style="left:517px" role="img" aria-label="Portrait photo of client Anna Voss"></div>
  <div class="avatar abs" style="left:593px" role="img" aria-label="Portrait photo of client Jonas Kern"></div>
  <div class="person abs" style="left:510px"><b>ANNA VOSS</b><small>CEO</small></div>
  <div class="person abs" style="left:586px"><b>JONAS KERN</b><small>DIRECTOR</small></div>

  <div class="pager abs" style="left:570px"><svg width="7" height="10" viewBox="0 0 7 10"><path d="M6 1L2 5l4 4" stroke="#fff" stroke-width="1.6" fill="none"/></svg></div>
  <div class="pager abs" style="left:604px"><svg width="7" height="10" viewBox="0 0 7 10"><path d="M1 1l4 4-4 4" stroke="#fff" stroke-width="1.6" fill="none"/></svg></div>
</section>

<footer class="footer abs">
  <div class="footer-logo abs"><i class="mark"></i><span class="name">Velmora Strom</span></div>

  <h4 class="abs" style="left:464px;top:56px">About us</h4>
  <div class="rule abs" style="left:464px;top:78px;width:286px"></div>
  <p class="about abs">We are a family-run master electrician business with years of experience in homes, shops and offices. Reliable work, fair prices and clean sites are our promise to you.</p>
  <div class="rule abs" style="left:464px;top:196px;width:286px"></div>
  <div class="connect abs">Connect with us <i></i><i></i><i></i></div>

  <h4 class="abs" style="left:809px;top:56px">Contact Information</h4>
  <div class="rule abs" style="left:809px;top:78px;width:230px"></div>
  <div class="row abs" style="top:101px"><svg width="16" height="16" viewBox="0 0 24 24"><rect x="1" y="1" width="22" height="22" rx="3" fill="#fff"/><path fill="#2b4d9c" d="M8 6.5l2 2-1.2 1.7a9 9 0 0 0 5 5l1.7-1.2 2 2-1.5 1.8c-5 0-10-5-10-10z"/></svg>Call: 000-000-0000</div>
  <div class="row abs" style="top:133px"><svg width="16" height="12" viewBox="0 0 16 12"><rect width="16" height="12" fill="#fff"/><path d="M0 0l8 6 8-6" stroke="#2b4d9c" stroke-width="1.4" fill="none"/></svg>email: <small>info@velmorastrom.de</small></div>
  <div class="row abs" style="top:165px"><svg width="16" height="16" viewBox="0 0 16 16"><circle cx="8" cy="8" r="7.5" fill="#fff"/><path d="M1 8h14M8 1c-3 3-3 11 0 14M8 1c3 3 3 11 0 14" stroke="#2b4d9c" fill="none"/></svg>website: <small>www.velmorastrom.de</small></div>
</footer>

<div class="copyright abs">© Copyright 2017 Velmora Strom. All Rights Reserved</div>

</body>
</html>
```